Website for boutique digital agency helping high-tech startups accelerate growth.

We need a website design for a relatively young company based in Mauritius called 'LumaTrel'.

We are a professional services firm delivering digital infrastructure for revenue operations (RevOps)*.

Entrepreneurial startups and SMBs in the technology sector work with us to accelerate growth by delivering extraordinary customer experiences across the full customer lifecycle.

We would like a colourful design that utilises the (4) colours of our existing logo design.

The final design should communicate dynamic growth through relentless customer focus.
----------------------------------------------------------
*Revenue Operations (RevOps) is the strategic alignment of sales, marketing and customer success operations to accelerate growth by delivering extraordinary customer experiences across the full customer life cycle.

Target Market(s)

Entrepreneurial startups and SMBs (Small/Medium Businesses) in the technology sector.

Question: Why the technology sector?

Answer: Because technology entrepreneurs often have a tremendous challenge to effectively communicate to the market and to prospective customers the value and the benefits of their products & services due to the inherent complexity of technological innovation.

LumaTrel is a team of creatively-minded engineers and technologists who have worked with and understand the technologies and innovations our clients are passionate about bringing to market.

Industry/Entity Type

Professional Service

Number of Pages Required

5+ page

Font styles to use
Sans Serif

Requirements
Must have
• Minimalistic designs rich with visual meaning are highly preferred. Mobile responsive designs are also required. Must show how designs render on Desktop, Tablet and Smartphone devices.

Website pages:
1) Homepage: problem statement, target customers, value proposition & benefits
2) Services: 3-4 tiers of services packages with pricing and "how to work with us"
3) Resources: links to all kinds of relevant materials
4) Contact Us: contact form and special project quote form
5) Blog: matrix design with featured images for each post
Nice to have
• Bold, interesting, colourful, inspiring images that visually communicate:
- relentless customer focus
- extraordinary, memorable experiences
- business at the speed of innovation
Should not have
• Any meme or theme that panders to "political correctness".

```html
<!DOCTYPE html>
<html lang="en">
<head>
<meta charset="utf-8">
<title>LumaTrel — Home</title>
<link href="https://fonts.googleapis.com/css2?family=Figtree:wght@400;500;600;700;800&display=swap" rel="stylesheet">
<style>
:root{
  --teal:#1a7f73;
  --teal-dark:#156b61;
  --ink:#1f1f24;
  --body:#55585e;
  --navy:#06182a;
  --navy-2:#0b2a45;
  --red:#e8112d;
  --orange:#f26a1b;
  --paper:#ffffff;
  --mist:#f7f7f7;
  --line:#e6e6e6;
}
*{box-sizing:border-box;margin:0;padding:0}
html,body{width:1200px;height:3877px;overflow:hidden;background:var(--paper)}
body{font-family:"Figtree",Arial,sans-serif;color:var(--ink);position:relative}
section,header,footer{position:relative;width:1200px}
.btn{display:inline-flex;align-items:center;gap:10px;background:var(--teal);color:#fff;font-weight:700;font-size:15px;text-decoration:none;border-radius:2px;padding:0 24px;height:40px;white-space:nowrap}
.btn svg{width:16px;height:16px}

/* nav */
.site-nav{height:77px;border-bottom:1px solid var(--line);display:flex;align-items:center;background:#fff}
.brand{position:absolute;left:86px;top:22px;display:flex;align-items:center;gap:10px;font-weight:700;font-size:20px;color:var(--ink)}
.brand-mark{width:22px;height:22px;background:var(--teal)}
.nav-links{position:absolute;left:505px;top:0;display:flex;height:77px}
.nav-links a{display:flex;align-items:center;height:77px;margin-right:54px;font-size:16px;font-weight:600;color:var(--ink);text-decoration:none;position:relative}
.nav-links a.active{color:var(--teal)}
.nav-links a.active::after{content:"";position:absolute;left:0;right:0;bottom:0;height:3px;background:var(--teal)}
.nav-cta{position:absolute;left:970px;top:18px;height:40px}

/* hero */
.hero{height:680px;overflow:hidden}
.hero-art{position:absolute;inset:0;background:radial-gradient(ellipse at 70% 35%,#123b5c 0%,var(--navy-2) 35%,var(--navy) 80%)}
.hero-content{position:absolute;left:0;right:0;top:220px;text-align:center;color:#fff}
.hero h1{font-size:37px;font-weight:700;line-height:1.42;width:640px;margin:0 auto}
.hero .btn{margin-top:40px;height:40px}

/* what we do */
.what-we-do{height:420px;background:#fff;border-bottom:1px solid var(--line)}
.wwd-decor{position:absolute;top:20px;width:110px;height:370px;background:radial-gradient(circle,#e3e3e3 0%,rgba(255,255,255,0) 70%)}
.wwd-decor.left{left:0}.wwd-decor.right{right:0}
.wwd-text{position:absolute;left:168px;top:30px;width:460px}
.section-title{font-size:28px;font-weight:800;text-transform:uppercase;letter-spacing:.2px}
.wwd-text p{margin-top:28px;font-size:16.5px;line-height:1.32;color:var(--body)}
.wwd-text strong{color:var(--teal);font-weight:700}
.wwd-text .btn{margin-top:42px}
.video-thumb{position:absolute;left:674px;top:58px;width:328px;height:258px;background:radial-gradient(ellipse at 48% 50%,#9a9a9a 0%,#3a3a3a 35%,#0c0c0c 80%)}
.play{position:absolute;left:130px;top:95px;width:68px;height:68px}

/* how we help */
.how-we-help{height:1300px;background:var(--mist)}
.how-we-help .section-title{position:absolute;top:42px;left:0;right:0;text-align:center;font-size:25px}
.lede{position:absolute;top:92px;left:330px;width:540px;text-align:center;font-size:16px;line-height:1.75;color:var(--body)}
.service{position:absolute;width:400px}
.service h3{font-size:21px;font-weight:700}
.service p{margin-top:18px;font-size:16px;line-height:1.78;color:var(--body)}
.service.marketing{left:148px;top:240px}.service.marketing h3{color:var(--teal)}
.service.sales{left:678px;top:640px}.service.sales h3{color:var(--red)}
.service.success{left:148px;top:1046px}.service.success h3{color:var(--orange)}
.illus{position:absolute;border-radius:6px}
.illus.one{left:710px;top:212px;width:300px;height:250px;background:linear-gradient(135deg,#eceff1,#dfe5e6 60%,#c9dcd9)}
.illus.two{left:168px;top:600px;width:270px;height:270px;background:linear-gradient(135deg,#e4e4e8,#d6d5dc 60%,#cfe2df)}
.illus.three{left:705px;top:1020px;width:320px;height:240px;background:linear-gradient(135deg,#eeeeee,#e1e3e4 60%,#c7ddd9)}
.connector{position:absolute;left:0;top:0;width:1200px;height:1300px}

/* blog */
.blog{height:570px;background:#fff;border-top:1px solid var(--line)}
.blog .section-title{position:absolute;top:26px;left:0;right:0;text-align:center;font-size:25px}
.post{position:absolute;top:82px;width:286px;height:430px;background:#fff;box-shadow:0 2px 10px rgba(0,0,0,.09);text-align:center}
.post:nth-of-type(1){left:128px}.post:nth-of-type(2){left:457px}.post:nth-of-type(3){left:786px}
.post-img{margin:14px 16px 0;height:190px}
.img-tunnel{background:radial-gradient(ellipse at 55% 55%,#d8d8d8 0%,#3b3b3b 35%,#060606 80%)}
.img-lights{background:linear-gradient(120deg,#ff4c6a 0%,#d1102a 45%,#5a0510 100%)}
.img-city{background:linear-gradient(180deg,#a9c4dc 0%,#d6e2ea 55%,#f2f4f5 100%)}
.post h4{margin-top:20px;font-size:15.5px;font-weight:800}
.post p{margin:8px 22px 0;font-size:13.5px;line-height:1.35;color:var(--body)}
.post .btn{margin-top:16px;height:36px;font-size:14px;padding:0 22px}

/* testimonials */
.testimonials{height:470px;background:var(--mist);border-top:1px solid var(--line)}
.testimonials .section-title{position:absolute;top:36px;left:0;right:0;text-align:center;font-size:25px}
.quote{position:absolute;left:357px;top:100px;width:486px;height:180px;background:#fff;box-shadow:0 2px 10px rgba(0,0,0,.08);padding:30px 34px;text-align:center;font-size:16px;line-height:1.35;color:#3e4045}
.quote::after{content:"";position:absolute;left:232px;bottom:-12px;width:22px;height:22px;background:#fff;transform:rotate(45deg);box-shadow:3px 3px 5px rgba(0,0,0,.05)}
.arrow{position:absolute;top:170px;width:24px;height:24px}
.arrow.prev{left:300px}.arrow.next{left:876px}
.author{position:absolute;left:496px;top:310px;display:flex;align-items:center;gap:18px}
.avatar{width:62px;height:62px;border-radius:50%;background:linear-gradient(135deg,#d9d9d9,#8a8a8a)}
.author b{display:block;font-size:17px;font-weight:500}
.author span{font-size:13px;color:var(--body)}

/* footer */
.site-footer{height:360px;background:var(--teal);color:#fff}
.foot-col{position:absolute;top:28px}
.foot-col h5{font-size:12.5px;font-weight:700;letter-spacing:.3px;margin-bottom:20px}
.foot-col a{display:block;color:#fff;text-decoration:none;font-size:12.5px;margin-bottom:17px;font-weight:500}
.col-services{left:129px}.col-company{left:398px}.col-connect{left:611px}.col-news{left:853px}
.socials{display:flex;gap:10px}
.socials span{width:16px;height:16px;background:#fff;border-radius:2px}
.newsletter{display:flex;width:218px;height:36px;border:1px solid #fff}
.newsletter span{flex:1;font-size:11px;padding:10px 6px;color:#bfe0db}
.newsletter i{width:44px;background:#fff;display:flex;align-items:center;justify-content:center}
.copyright{position:absolute;left:0;right:0;bottom:28px;text-align:center;font-size:11.5px}
</style>
</head>
<body>

<header class="site-nav">
  <div class="brand"><span class="brand-mark"></span>lumatrel.io</div>
  <nav class="nav-links">
    <a href="#" class="active">Home</a>
    <a href="#">Services</a>
    <a href="#">Resources</a>
    <a href="#">Blog</a>
  </nav>
  <a href="#" class="btn nav-cta">Contact Us
    <svg viewBox="0 0 16 16" fill="none" stroke="#fff" stroke-width="1.8"><path d="M2 8h11M9 4l4 4-4 4"/></svg></a>
</header>

<section class="hero">
  <div class="hero-art" role="img" aria-label="Dark blue digital network of glowing points joined by fine lines"></div>
  <div class="hero-content">
    <h1>We drive growth through operational efficiency across the customer lifecycle.</h1>
    <a href="#" class="btn">Find Out More
      <svg viewBox="0 0 16 16" fill="none" stroke="#fff" stroke-width="1.8"><path d="M2 8h11M9 4l4 4-4 4"/></svg></a>
  </div>
</section>

<section class="what-we-do">
  <div class="wwd-decor left" role="img" aria-label="Faint grey network of dots"></div>
  <div class="wwd-decor right" role="img" aria-label="Faint grey network of dots"></div>
  <div class="wwd-text">
    <h2 class="section-title">What we do</h2>
    <p><strong>LumaTrel's</strong> expertise with the world's leading cloud CRM platform (Cloudora) provides the foundation for innovative solutions to the most challenging problems companies face when seeking to achieve greater business success. Our passion is helping our clients achieve their success potential through strategic application of web, cloud and mobile technologies.</p>
    <a href="#" class="btn">Learn More
      <svg viewBox="0 0 16 16" fill="none" stroke="#fff" stroke-width="1.8"><path d="M2 8h11M9 4l4 4-4 4"/></svg></a>
  </div>
  <div class="video-thumb" role="img" aria-label="Black and white video still of a light tunnel">
    <svg class="play" viewBox="0 0 68 68" fill="none" stroke="#fff" stroke-width="2"><circle cx="34" cy="34" r="32"/><path d="M27 21l20 13-20 13z"/></svg>
  </div>
</section>

<section class="how-we-help">
  <h2 class="section-title">How we help your business grow</h2>
  <p class="lede">Lorem ipsum dolor sit amet, consetetur sadips elitr, sed diam nonumy eirmod tempor invidunt.</p>

  <svg class="connector" viewBox="0 0 1200 1300" fill="none" stroke="#333" stroke-width="1.3">
    <g stroke-dasharray="6 5">
      <path d="M308 450 C330 560 420 565 560 562 C660 560 710 580 726 625"/>
      <path d="M726 862 C700 940 600 950 470 955 C360 960 310 980 308 1020"/>
    </g>
    <g fill="#f7f7f7">
      <circle cx="308" cy="445" r="4.5"/><circle cx="728" cy="630" r="4.5"/>
      <circle cx="728" cy="857" r="4.5"/><circle cx="308" cy="1025" r="4.5"/>
    </g>
  </svg>

  <div class="service marketing">
    <h3>Marketing</h3>
    <p>Lorem ipsum dolor sit amet, consetetur sadips elitr, sed diam nonumy eirmod tempor invidunt ut labore et dolore magna aliquyam erat, sed diam voluptua. At vero eos et accusam.</p>
  </div>
  <div class="illus one" role="img" aria-label="Illustration of a person presenting pie and bar charts"></div>

  <div class="illus two" role="img" aria-label="Illustration of a person drawing a growth line on a board"></div>
  <div class="service sales">
    <h3>Sales</h3>
    <p>Lorem ipsum dolor sit amet, consetetur sadips elitr, sed diam nonumy eirmod tempor invidunt ut labore et dolore magna aliquyam erat, sed diam voluptua. At vero eos et accusam.</p>
  </div>

  <div class="service success">
    <h3>Customer success</h3>
    <p>Lorem ipsum dolor sit amet, consetetur sadips elitr, sed diam nonumy eirmod tempor invidunt ut labore et dolore magna aliquyam erat, sed diam voluptua. At vero eos et accusam.</p>
  </div>
  <div class="illus three" role="img" aria-label="Illustration of a person beside a large pie chart"></div>
</section>

<section class="blog">
  <h2 class="section-title">Latest blog posts</h2>
  <article class="post">
    <div class="post-img img-tunnel" role="img" aria-label="Black and white light tunnel"></div>
    <h4>LOREM IPSUM DOLOR SIT</h4>
    <p>Lorem ipsum dolor sit amet, cons sadipscing elitr, sed diam nonumy eirmod tempor invidunt ut</p>
    <a href="#" class="btn">Learn More <svg viewBox="0 0 16 16" fill="none" stroke="#fff" stroke-width="1.8"><path d="M2 8h11M9 4l4 4-4 4"/></svg></a>
  </article>
  <article class="post">
    <div class="post-img img-lights" role="img" aria-label="Rows of red glowing lights"></div>
    <h4>LOREM IPSUM DOLOR SIT</h4>
    <p>Lorem ipsum dolor sit amet, cons sadipscing elitr, sed diam nonumy eirmod tempor invidunt ut</p>
    <a href="#" class="btn">Learn More <svg viewBox="0 0 16 16" fill="none" stroke="#fff" stroke-width="1.8"><path d="M2 8h11M9 4l4 4-4 4"/></svg></a>
  </article>
  <article class="post">
    <div class="post-img img-city" role="img" aria-label="City towers rising above clouds"></div>
    <h4>LOREM IPSUM DOLOR SIT</h4>
    <p>Lorem ipsum dolor sit amet, cons sadipscing elitr, sed diam nonumy eirmod tempor invidunt ut</p>
    <a href="#" class="btn">Learn More <svg viewBox="0 0 16 16" fill="none" stroke="#fff" stroke-width="1.8"><path d="M2 8h11M9 4l4 4-4 4"/></svg></a>
  </article>
</section>

<section class="testimonials">
  <h2 class="section-title">What did our clients say?</h2>
  <svg class="arrow prev" viewBox="0 0 24 24" fill="none" stroke="#111" stroke-width="2.4"><path d="M16 3l-9 9 9 9"/></svg>
  <blockquote class="quote">Lorem ipsum dolor sit amet, consetetur sadipscing elitr, sed diam nonumy eirmod tempor invidunt ut labore et dolore magna aliquyam erat, sed diam voluptua. At vero eos et accusam et justo duo dolores et ea rebum. Stet clita kasd gubergren.</blockquote>
  <svg class="arrow next" viewBox="0 0 24 24" fill="none" stroke="#111" stroke-width="2.4"><path d="M8 3l9 9-9 9"/></svg>
  <div class="author">
    <div class="avatar" role="img" aria-label="Client portrait"></div>
    <div><b>Daniel Reyes, CTO</b><span>Northvale</span></div>
  </div>
</section>

<footer class="site-footer">
  <div class="foot-col col-services">
    <h5>SERVICES</h5>
    <a href="#">BOOK AN APPOINTMENT</a><a href="#">WHAT WE DO</a><a href="#">BUSINESS SERVICES</a><a href="#">PRIVACY POLICY</a><a href="#">ABOUT US</a>
  </div>
  <div class="foot-col col-company">
    <h5>COMPANY</h5>
    <a href="#">RESOURCES</a><a href="#">BLOG</a><a href="#">CAREERS</a><a href="#">CONTACT</a>
  </div>
  <div class="foot-col col-connect">
    <h5>CONNECT WITH US</h5>
    <div class="socials"><span></span><span></span><span></span><span></span></div>
  </div>
  <div class="foot-col col-news">
    <h5>JOIN OUR NEWS LETTER</h5>
    <div class="newsletter"><span>name@example.com</span>
      <i><svg width="18" height="14" viewBox="0 0 18 14" fill="none" stroke="#1a7f73" stroke-width="1.5"><rect x="1" y="1" width="16" height="12"/><path d="M1 1l8 7 8-7"/></svg></i></div>
  </div>
  <p class="copyright">Copyright LumaTrel @ 2020</p>
</footer>

</body>
</html>
```